Kestrel Summit 2019 Enemies of the End-Times Church Flyer

We want a church conference flyer designed. We are looking for a professional, yet catchy design that uses our brand colors and logo creatively while communicating key information of the event effectively. <br/>The flyer must include all of the following:<br/>Title: Kestrel Summit 2019<br/>Topic: The Enemies of The End-Times Church <br/>Subtitles: <br/> -How the antichrist raises an army by social behavior engineering. <br/>-How the architects of modern social constructs escaped the church's radar. <br/>-The Holy Spirit's end-times agenda:<br/> The Knock-Out Punch!<br/>Speaker: Prophet Marcus Toliver <br/>Dates/time: December 27, 28 & 29 at 6pm<br/>Location: Halvorn Community Center <br/> 241 Pellham Street <br/> Portland, ME 04102<br/>Contact info: phone: 207-555-0148 <br/>email: contact@brookmeadow.example <br/> www.vutel.example<br/>*The flyer must also include a picture of the speaker and our Vutel logo <br/>Thanks, we look forward to seeing what you come up with!

Colors

Designer to choose colors to be used in the design.

Requirements
Must have
• The flyer must include all of the following:
• Title: Kestrel Summit 2019
• Topic: The Enemies of The End-Times Church
• Subtitles:
• -How the antichrist raises an army by social behavior engineering.
• -How the architects of modern social constructs escaped the church's radar.
• -The Holy Spirit's end-times agenda:
• The Knock-Out Punch!
• Speaker: Prophet Marcus Toliver
• Dates/time: December 27, 28 & 29 at 6pm
• Location: Halvorn Community Center
• 241 Pellham Street
• Portland, ME 04102
• Contact info: phone: 207-555-0148
• email: contact@brookmeadow.example
• www.vutel.example
• *The flyer must also include a picture of the speaker and our Vutel logo
Should not have
• Pictures of crosses or church buildings

```html
<!DOCTYPE html>
<html lang="en">
<head>
<meta charset="utf-8">
<title>Kestrel Summit 2019 – The Enemies of The End-Times Church</title>
<link rel="stylesheet" href="https://fonts.googleapis.com/css2?family=Rubik:wght@300;400;500;700;800&family=Overpass:wght@400;600;700;800&display=swap">
<style>
  :root {
    --navy: #0b3a5e;
    --orange: #f3992b;
    --orange-light: #f8ad55;
    --orange-deep: #d9801c;
    --ink: #2a2a2a;
    --white: #ffffff;
    --page: #ffffff;
  }
  * { box-sizing: border-box; margin: 0; padding: 0; }
  html, body { width: 847px; height: 1200px; overflow: hidden; background: var(--page); }
  .flyer {
    position: absolute; left: 12px; top: 10px; width: 816px; height: 1172px;
    background: var(--orange); overflow: hidden;
    font-family: "Overpass", "Rubik", sans-serif; color: var(--ink);
  }
  .flyer__backdrop { position: absolute; left: 0; top: 0; width: 816px; height: 420px; }
  .event-title {
    position: absolute; left: 32px; top: 36px; width: 784px; height: 66px;
    background: var(--orange-light);
    font-family: "Rubik", sans-serif; font-size: 52px; line-height: 66px;
    color: var(--white); padding-left: 14px; white-space: nowrap;
    text-shadow: 2px 2px 0 #3a2a1a;
  }
  .event-title strong { font-weight: 800; letter-spacing: 0.5px; }
  .event-title span { font-weight: 400; }
  .topic {
    position: absolute; left: 36px; top: 132px;
    font-family: "Rubik", sans-serif; font-weight: 700; font-size: 58px; line-height: 62px;
    color: var(--white);
  }
  .topic .light { font-weight: 300; }
  .subtitle-bar {
    position: absolute; left: 0; width: 780px;
    background: var(--orange-light);
    border-radius: 0 0 120px 0 / 0 0 40px 0;
    box-shadow: 0 3px 4px rgba(120, 60, 0, 0.35);
    font-weight: 700; font-size: 16px; color: var(--ink);
    padding-left: 36px;
  }
  .subtitle-bar--one { top: 394px; height: 36px; line-height: 40px; }
  .subtitle-bar--two { top: 442px; height: 36px; line-height: 40px; }
  .subtitle-bar--agenda { top: 490px; height: 106px; border-radius: 0 120px 0 0 / 0 30px 0 0; padding-top: 12px; }
  .agenda__lead { font-family: "Rubik", sans-serif; font-weight: 400; font-size: 30px; line-height: 36px; }
  .agenda__punch { font-family: "Rubik", sans-serif; font-weight: 400; font-size: 42px; line-height: 50px; color: var(--navy); }
  .details { position: absolute; left: 36px; top: 636px; width: 480px; }
  .details dt { font-weight: 700; font-size: 16px; color: var(--white); line-height: 20px; margin-top: 12px; }
  .details dt:first-child { margin-top: 0; }
  .details dd { font-size: 23px; line-height: 28px; color: var(--ink); }
  .details b { font-weight: 800; }
  .speaker { position: absolute; left: 538px; top: 644px; width: 242px; }
  .speaker__photo {
    width: 242px; height: 264px; border: 3px solid var(--white);
    background: linear-gradient(160deg, #6e6a64 0%, #3b3230 55%, #7a2a24 100%);
  }
  .speaker__label { font-weight: 700; font-size: 16px; color: var(--white); line-height: 20px; margin-top: 8px; }
  .speaker__name { font-size: 23px; line-height: 28px; }
  .footer { position: absolute; left: 0; top: 993px; width: 816px; height: 179px; background: var(--navy); }
  .footer__web { position: absolute; left: 36px; top: 112px; color: var(--white); font-size: 17px; }
  .brand {
    position: absolute; left: 683px; top: 24px; width: 96px; height: 96px;
    background: var(--white); display: flex; align-items: center; justify-content: center;
    font-family: "Rubik", sans-serif; font-weight: 500; font-size: 24px; color: var(--navy);
  }
</style>
</head>
<body>
<main class="flyer">
  <svg class="flyer__backdrop" viewBox="0 0 816 420" aria-hidden="true">
    <path d="M0 0 H660 C640 230 430 372 0 378 Z" fill="#c8761a" opacity="0.55"/>
    <path d="M0 0 H650 C625 220 420 358 0 364 Z" fill="var(--navy)"/>
  </svg>

  <h1 class="event-title"><strong>KESTREL SUMMIT</strong> <span>2019</span></h1>

  <h2 class="topic">The Enemies <span class="light">of</span><br>The End-Times<br>Church</h2>

  <p class="subtitle-bar subtitle-bar--one">How the antichrist raises an army by social behavior engineering.</p>
  <p class="subtitle-bar subtitle-bar--two">How the architects of modern social constructs escaped the church's radar.</p>
  <div class="subtitle-bar subtitle-bar--agenda">
    <p class="agenda__lead">The Holy Spirit's end-times agenda</p>
    <p class="agenda__punch">The Knock-Out Punch!</p>
  </div>

  <dl class="details">
    <dt>Dates/time:</dt>
    <dd>December <b>27, 28 &amp; 29</b> at <b>6pm</b></dd>
    <dt>Location:</dt>
    <dd>Halvorn Community Center<br>241 Pellham Street<br>Portland, ME 04102</dd>
    <dt>Contact info:</dt>
    <dd>phone: <b>207-555-0148</b></dd>
    <dt>email:</dt>
    <dd>contact@brookmeadow.example</dd>
  </dl>

  <figure class="speaker">
    <div class="speaker__photo" role="img" aria-label="Portrait photo of the speaker, Prophet Marcus Toliver, in front of bookshelves"></div>
    <figcaption>
      <p class="speaker__label">Speaker:</p>
      <p class="speaker__name">Prophet Marcus Toliver</p>
    </figcaption>
  </figure>

  <footer class="footer">
    <p class="footer__web">www.vutel.example</p>
    <div class="brand">Vutel</div>
  </footer>
</main>
</body>
</html>
```